Environmental and Industrial Services Company Needs Brochure Design

We need a new brochure design for an established company that services the Southeastern United States. It is a highly diversified company that centers around Environmental and Industrial Services. The Environmental side revolved around emergency chemical and spill response, HAZMAT, hazardous/ non hazardous waste management, wastewater treatment, and remediation services (cleaning up contaminated sites). And the Industrial side utilizes heavy equipment like vacuum trucks and hydroblasters to clean process equipment inside of factories and manufacturing facilities. Predominantly our clients are large industrial clients, commercial clients, and the government. The people who would see the brochure are decision makers; engineers, project managers, procurement heads for large companies. These are serious and educated people who are looking for the best.

The designs should incorporate our colors and I welcome you to use any of the pictures from our website www.kdlpurex.com EXCLUSIVELY FOR THIS PROJECT, of course. This brochure should communicate professionalism, confidence, stability, and portray the kind of company who efficiently manages complicated issues. Our site gives a better kind of idea of the branding we want to extend into the brochure and I caution any designer to NOT allow the environmental aspect of our company to lead them to design brochures more fitting for Green Tech companies or Alternative Energy.

Target Market(s)

Engineers, Factory Managers, Project Managers, Consultants, Heads of Large Companies, Service Managers

Industry/Entity Type

Industrial

Requirements
Must have
• The brochure must
-Be divided like the services section of our website w/ categories in this order:
-Industrial Services, Waste Management, Remediation Services, Emergency Response, Marine Services, Stormwater Services
-Owing to the large info in these sections, I'd recommend separate pages or tabs
-Incorporate our colors
-Use photos from the site

```html
<!DOCTYPE html>
<html lang="en">
<head>
<meta charset="utf-8">
<title>Company Brochure – Front, Inside and Back</title>
<link rel="stylesheet" href="https://fonts.googleapis.com/css2?family=Michroma&family=Marcellus&display=swap">
<style>
  :root {
    --blue-deep: #1f62a6;
    --blue-mid: #1a86cf;
    --blue-bright: #18b8ee;
    --heading-blue: #2f6aa8;
    --ink: #1e1e1e;
    --body-ink: #5a5a5a;
    --slate: #5c5c5c;
    --paper: #f7f7f7;
    --stage-light: #f6f6f6;
    --stage-dark: #e4e4e4;
    --label-ink: #333333;
  }
  html, body {
    margin: 0;
    padding: 0;
    overflow: hidden;
  }
  .canvas {
    position: relative;
    width: 1200px;
    height: 890px;
    overflow: hidden;
    background: radial-gradient(ellipse at 50% 40%, var(--stage-light) 0%, var(--stage-dark) 100%);
    font-family: "Marcellus", serif;
  }
  .panel {
    position: absolute;
    width: 260px;
    height: 519px;
    background: linear-gradient(180deg, #ffffff 0%, var(--paper) 60%, #ededed 100%);
    box-shadow: 0 6px 14px rgba(0,0,0,0.28), 0 0 4px rgba(0,0,0,0.12);
    overflow: hidden;
  }
  .panel svg.panel-art {
    position: absolute;
    inset: 0;
    width: 260px;
    height: 519px;
  }
  .panel-front { left: 40px; top: 173px; }
  .panel-about { left: 328px; top: 177px; }
  .panel-services { left: 615px; top: 173px; }
  .panel-back { left: 894px; top: 175px; }

  .logo-note {
    position: absolute;
    font-size: 9px;
    color: #ffffff;
    white-space: nowrap;
  }
  .front-title {
    position: absolute;
    left: 105px;
    top: 94px;
    font-size: 19px;
    color: var(--heading-blue);
    white-space: nowrap;
  }
  .logo-placeholder {
    position: absolute;
    font-size: 19px;
    white-space: nowrap;
  }
  .front-logo { left: 114px; top: 239px; color: var(--ink); }
  .footer-logo { right: 6px; bottom: 6px; color: #ffffff; font-size: 16px; }

  .panel-heading {
    position: absolute;
    font-family: "Michroma", sans-serif;
    font-size: 19px;
    color: var(--ink);
    white-space: nowrap;
    letter-spacing: -0.3px;
  }
  .entry {
    position: absolute;
    left: 20px;
    right: 8px;
  }
  .entry-title {
    font-family: "Michroma", sans-serif;
    font-size: 10.5px;
    color: var(--heading-blue);
    margin: 0 0 6px 2px;
    font-weight: normal;
  }
  .entry-text {
    font-size: 8.2px;
    line-height: 10px;
    color: var(--body-ink);
    margin: 0 0 3px 0;
    white-space: nowrap;
  }
  .photo-strip {
    position: absolute;
    left: 0;
    width: 260px;
    height: 106px;
  }
  .photo {
    position: absolute;
    top: 0;
    height: 106px;
  }
  .photo-truck {
    left: 2px;
    width: 138px;
    background: linear-gradient(180deg, #c8d3dc 0%, #aeb6b2 55%, #8e9486 100%);
  }
  .photo-crew {
    left: 142px;
    width: 118px;
    background: linear-gradient(160deg, #9a8f83 0%, #b77450 55%, #6f645c 100%);
  }
  .photo-fade {
    position: absolute;
    inset: 0;
    background: linear-gradient(180deg, rgba(247,247,247,0.55) 0%, rgba(247,247,247,0.15) 100%);
  }

  .contact-heading {
    position: absolute;
    left: 25px;
    top: 46px;
    font-family: "Michroma", sans-serif;
    font-size: 15.5px;
    color: var(--heading-blue);
    white-space: nowrap;
  }
  .contact-block {
    position: absolute;
    left: 16px;
    font-size: 12.5px;
    line-height: 14.5px;
    color: var(--body-ink);
    margin: 0;
    font-style: normal;
  }
  .service-photo {
    position: absolute;
    left: 0;
    width: 186px;
  }
  .service-photo span {
    position: absolute;
    left: 0;
    right: 0;
    bottom: 3px;
    text-align: center;
    font-family: "Michroma", sans-serif;
    font-size: 6px;
    color: #ffffff;
    letter-spacing: 0.2px;
  }
  .photo-industrial { top: 295px; height: 60px; background: linear-gradient(180deg, #3d6f9c 0%, #5b6b78 60%, #2f3a44 100%); }
  .photo-spill { top: 357px; height: 56px; background: linear-gradient(180deg, #6fa9d4 0%, #d88a2a 55%, #c2a56a 100%); }
  .photo-remediation { top: 414px; height: 52px; background: linear-gradient(180deg, #9cb3c8 0%, #c29a4a 55%, #6b5a3c 100%); }
  .photo-waste { top: 467px; height: 52px; background: linear-gradient(180deg, #8a5a34 0%, #b4652c 55%, #5f4a36 100%); }

  .view-label {
    position: absolute;
    font-family: "Michroma", sans-serif;
    color: var(--label-ink);
    white-space: nowrap;
  }
  .label-front { left: 118px; top: 755px; font-size: 31px; }
  .label-inside { left: 438px; top: 756px; font-size: 35px; }
  .label-back { left: 988px; top: 757px; font-size: 31px; }
</style>
</head>
<body>
<main class="canvas">

  <!-- Front cover -->
  <section class="panel panel-front">
    <svg class="panel-art" viewBox="0 0 260 519" aria-hidden="true">
      <defs>
        <linearGradient id="frontBlue" x1="0" y1="0" x2="0" y2="1">
          <stop offset="0" stop-color="var(--blue-deep)"/>
          <stop offset="0.45" stop-color="var(--blue-bright)"/>
          <stop offset="1" stop-color="var(--blue-deep)"/>
        </linearGradient>
        <linearGradient id="curveShade" x1="0" y1="0" x2="1" y2="0">
          <stop offset="0" stop-color="#000" stop-opacity="0.18"/>
          <stop offset="1" stop-color="#000" stop-opacity="0"/>
        </linearGradient>
      </defs>
      <path d="M60 345 C140 315 210 302 260 297 V519 H60 Z" fill="var(--slate)"/>
      <path d="M112 0 C82 80 62 190 68 262 C74 330 96 360 88 405 C82 450 100 495 118 519 H0 V0 Z" fill="url(#curveShade)" transform="translate(8,0)"/>
      <path d="M112 0 C82 80 62 190 68 262 C74 330 96 360 88 405 C82 450 100 495 118 519 H0 V0 Z" fill="url(#frontBlue)"/>
    </svg>
    <p class="logo-note" style="left:5px; top:18px; margin:0;">Logo Icon Only here</p>
    <h1 class="front-title" style="margin:0; font-weight:normal;">Company Profile</h1>
    <p class="logo-placeholder front-logo" style="margin:0;">Your Logo here</p>
  </section>

  <!-- Inside: About Us -->
  <section class="panel panel-about">
    <h2 class="panel-heading" style="left:50px; top:38px; margin:0; font-weight:normal;">About Us</h2>
    <div class="entry" style="top:83px;">
      <p class="entry-text">Lorem ipsum dolor sit amet, consectetur adipisicing elit, sed<br>do eiusmod tempor incididunt ut labore et dolore magna</p>
      <p class="entry-text">Lorem ipsum dolor sit amet, consectetur adipisicing elit, sed<br>do eiusmod tempor incididunt ut labore et dolore magna</p>
    </div>
    <div class="entry" style="top:144px;">
      <h3 class="entry-title">Mission</h3>
      <p class="entry-text">Lorem ipsum dolor sit amet, consectetur adipisicing elit, sed<br>do eiusmod tempor incididunt ut labore et dolore magna</p>
    </div>
    <div class="entry" style="top:199px;">
      <h3 class="entry-title">Vision</h3>
      <p class="entry-text">Lorem ipsum dolor sit amet, consectetur adipisicing elit, sed<br>do eiusmod tempor incididunt ut labore et dolore magna</p>
    </div>
    <div class="entry" style="top:258px;">
      <h3 class="entry-title">Objectives</h3>
      <p class="entry-text">Lorem ipsum dolor sit amet, consectetur adipisicing elit, sed<br>do eiusmod tempor incididunt ut labore et dolore magna</p>
    </div>
    <div class="entry" style="top:315px;">
      <h3 class="entry-title">Expertise</h3>
      <p class="entry-text">Lorem ipsum dolor sit amet, consectetur adipisicing elit, sed<br>do eiusmod tempor incididunt ut labore et dolore magna</p>
    </div>
    <div class="photo-strip" style="top:355px;">
      <div class="photo photo-truck" role="img" aria-label="Photo of a white vacuum truck parked at a job site"></div>
      <div class="photo photo-crew" role="img" aria-label="Photo of a spill response crew member in orange protective gear"></div>
      <div class="photo-fade"></div>
    </div>
    <svg class="panel-art" viewBox="0 0 260 519" aria-hidden="true">
      <defs>
        <linearGradient id="waveBlueA" x1="0" y1="0" x2="1" y2="0">
          <stop offset="0" stop-color="var(--blue-deep)"/>
          <stop offset="0.55" stop-color="var(--blue-bright)"/>
          <stop offset="1" stop-color="var(--blue-mid)"/>
        </linearGradient>
      </defs>
      <path d="M0 458 C70 462 130 492 190 480 C225 472 245 462 260 460 V519 H0 Z" fill="url(#waveBlueA)"/>
    </svg>
    <p class="logo-placeholder footer-logo" style="margin:0;">Your Logo here</p>
  </section>

  <!-- Inside: Our Services -->
  <section class="panel panel-services">
    <h2 class="panel-heading" style="left:50px; top:37px; margin:0; font-weight:normal;">Our Services</h2>
    <div class="entry" style="top:89px;">
      <h3 class="entry-title">Industrial Services</h3>
      <p class="entry-text">Lorem ipsum dolor sit amet, consectetur adipisicing elit, sed<br>do eiusmod tempor incididunt ut labore et dolore magna</p>
    </div>
    <div class="entry" style="top:145px;">
      <h3 class="entry-title">Waste Management</h3>
      <p class="entry-text">Lorem ipsum dolor sit amet, consectetur adipisicing elit, sed<br>do eiusmod tempor incididunt ut labore et dolore magna</p>
    </div>
    <div class="entry" style="top:200px;">
      <h3 class="entry-title">Remadiation</h3>
      <p class="entry-text">Lorem ipsum dolor sit amet, consectetur adipisicing elit, sed<br>do eiusmod tempor incididunt ut labore et dolore magna</p>
    </div>
    <div class="entry" style="top:259px;">
      <h3 class="entry-title">Emergency Response</h3>
      <p class="entry-text">Lorem ipsum dolor sit amet, consectetur adipisicing elit, sed<br>do eiusmod tempor incididunt ut labore et dolore magna</p>
    </div>
    <div class="photo-strip" style="top:356px;">
      <div class="photo photo-truck" role="img" aria-label="Photo of a white vacuum truck parked at a job site"></div>
      <div class="photo photo-crew" role="img" aria-label="Photo of a spill response crew member in orange protective gear"></div>
      <div class="photo-fade"></div>
    </div>
    <div class="entry" style="top:316px;">
      <h3 class="entry-title">Marine Services</h3>
      <p class="entry-text">Lorem ipsum dolor sit amet, consectetur adipisicing elit, sed<br>do eiusmod tempor incididunt ut labore et dolore magna</p>
    </div>
    <div class="entry" style="top:374px;">
      <h3 class="entry-title">StormWater Services</h3>
      <p class="entry-text">Lorem ipsum dolor sit amet, consectetur adipisicing elit, sed<br>do eiusmod tempor incididunt ut labore et dolore magna</p>
    </div>
    <svg class="panel-art" viewBox="0 0 260 519" aria-hidden="true">
      <defs>
        <linearGradient id="waveBlueB" x1="0" y1="0" x2="1" y2="0">
          <stop offset="0" stop-color="var(--blue-deep)"/>
          <stop offset="0.55" stop-color="var(--blue-bright)"/>
          <stop offset="1" stop-color="var(--blue-mid)"/>
        </linearGradient>
      </defs>
      <path d="M0 458 C70 462 130 492 190 480 C225 472 245 462 260 460 V519 H0 Z" fill="url(#waveBlueB)"/>
    </svg>
    <p class="logo-placeholder footer-logo" style="margin:0;">Your Logo here</p>
  </section>

  <!-- Back cover -->
  <section class="panel panel-back">
    <svg class="panel-art" viewBox="0 0 260 519" aria-hidden="true">
      <defs>
        <linearGradient id="backBlue" x1="0" y1="0" x2="0" y2="1">
          <stop offset="0" stop-color="var(--blue-deep)"/>
          <stop offset="0.5" stop-color="var(--blue-bright)"/>
          <stop offset="1" stop-color="var(--blue-deep)"/>
        </linearGradient>
      </defs>
      <path d="M151 0 C180 80 198 170 197 260 C196 360 162 440 155 519 H260 V0 Z" fill="#000" fill-opacity="0.12" transform="translate(-7,0)"/>
      <path d="M151 0 C180 80 198 170 197 260 C196 360 162 440 155 519 H260 V0 Z" fill="url(#backBlue)"/>
    </svg>
    <h2 class="contact-heading" style="margin:0; font-weight:normal;">Contact info</h2>
    <address class="contact-block" style="top:102px;">Abc Road, Abc Town<br>New York, USA</address>
    <p class="contact-block" style="top:141px;">Tel # 0000000000<br>Fax # 0000000000<br>Email Id: abc@abc.com<br>Website: www.abc.com</p>
    <div class="service-photo photo-industrial" role="img" aria-label="Photo of industrial plant piping and equipment"><span>INDUSTRIAL SERVICES</span></div>
    <div class="service-photo photo-spill" role="img" aria-label="Photo of an orange spill containment boom on water"><span>EMERGENCY SPILL RESPONSE LAND + WATER</span></div>
    <div class="service-photo photo-remediation" role="img" aria-label="Photo of an excavator loading a dump truck at a remediation site"><span>REMEDIATION SERVICES</span></div>
    <div class="service-photo photo-waste" role="img" aria-label="Photo of rusted waste drums stacked together"><span>WASTE MANAGEMENT</span></div>
    <p class="logo-note" style="left:163px; top:498px; margin:0;">Logo Icon Only here</p>
  </section>

  <p class="view-label label-front" style="margin:0;">Front</p>
  <p class="view-label label-inside" style="margin:0;">Brochure inside</p>
  <p class="view-label label-back" style="margin:0;">Back</p>
</main>
</body>
</html>
```